labels loose leaf tea business

I am in need of a label redo! I have attatched a couple of our old logo labels (still currently using these labels) also i have our new logo that we have loaded on the website feel free to look. www.brewlark.com i bought the business a year ago and have been wanting to get a new look for a minimal cost.we use the labels that are 4' by 3 1/3' on the bags that hold 100 grams the bag is 5.25"x 8 "stand up pouch and the smaller bag which is 4.25x 6.75" we have used a 2x2 label (which doesn't have room for as much detail. the bags are a matte silver at the time.
i am considering going to either a matte white or there is an aqua co lour not sure if that would work or there is a nice white or silver grey rice paper looking bag i am getting prices.
i would consider a larger label format on this bag as well for retail i need my logo the address and the telephone and website all the ingredients as well as tea type and caffiene content i like to include a short description of the tea, as well as country of origin could be fun.. i have included the steep time and possibly this is something to take into consideration is to make a small info graphic of the steep times that is the same sticker to go on the reverse side of each bag the same.could include the address and website... as you can see my bags have had a different color banner per the type of tea Which my customers are used to that idea pink means fruit black is abrown label blue is herbal etc.
to say what is my style is kind of hard for me i included the two pieces of art work from Northgate Printworks ...the coffee label i liked the bottom part simple and straight forward, (i could also look into seeing how much it would cost to heat stamp my logo on each bag) the second one i do kind of like had drawn also sort of vintage the new logo being aqua and grey to me is fresh and light....really i don't like busy or fussy or Victorian i like a bit unusual ( like the sticker on the kraft paper bag! but it could be a pain to put on straight every time i think the one on the biscotti (art image 3) is kind of neat how its applied the other way...
Anyway my market is some retail/ farmers markets etc.. and website.as well as our own retail shop.we have about 90 kinds of tea so i need to be able to edit and print these myself as to hold stock on labels is not cost effective.
i also should say we use the 4 oz metal tins which i use the same labels size as the large bag but mayb we could design it to fit around the whole tin.
well i hope this is enough info for you and i am super excited to see the products you come up with

Project Deadline Extended Reason: Thank you for taking time to look at my design project. i feel to extend the time as i have never done this before and realize some of you may have better ideas then i have and i feel like you may need more time as well and i have also been talking to some product manufacturers such as the pouches and printer and label makers, i think if possible i will head in the direction of getting a stock label printed where the basic information is pre-printed and i can just change the product detail AS needed.This however may throw a different twist on the labels as i'm not sure that the colored banner such as i had is the way to go.i can see potential in a couple of the designs.However much i wish i could get my logo preprinted ont he bags its not an option at this point its too pricy...so yay keep the designs coming we aren't finished yet! Added Sunday, February 12, 2017

Project Deadline Extended Reason: i am giving five more days, my reason being i have been ill and dont feel like i have the energy to give my full attention too the project as well as we have a wedding on the weekend...i see some close competiton here....and am getting excited as well as nervous as how i will really pick between so many cool designs Added Thursday, February 16, 2017

Project Deadline Extended
Reason: one more deadline... giving some of you designers a chance to get them in that had started on the designs please know this is the last extension and i am not super super excited about any of them yet.....i am looking for a label that can be changed up for the different tea types such as Tamsin provided so far.... so let your imaginations go and become creative, thanks for all the awesome effort so far.....

Target Market(s)

website,farmers markets, retail...seems to cover a broad spectrum of ages

Industry/Entity Type

Business

Colors
86cfc6

Requirements
Must have
• Brewlark is the name
• www.brewlark.com website
• packaged and blended in Canada
• Linden Alberta
• 403-718-2045
• 100 grams or 50 grams
• Tea type and name
• the steeping time and water temp and amount of tea
Nice to have
• Discover loose leaf tea at its brightest i s on the logo
• wouldn't have to have it there could take off and put somewhere else
• description of the tea as seen on the old tea labels i would like included

```html
<!DOCTYPE html>
<html lang="en">
<head>
<meta charset="utf-8">
<title>Brewlark Tea Label – Blueberry Burst</title>
<link rel="stylesheet" href="https://fonts.googleapis.com/css2?family=Lilita+One&family=Roboto:wght@400&display=swap">
<style>
  :root {
    --teal: #3a9e8a;
    --charcoal: #323232;
    --leaf-tone: #45534f;
    --white: #ffffff;
    --paper: #ffffff;
  }
  html, body {
    margin: 0;
    padding: 0;
    width: 1200px;
    height: 750px;
    overflow: hidden;
    background: var(--paper);
  }
  .label-sheet { display: block; width: 1200px; height: 750px; }
  .frame-line { stroke: var(--teal); fill: none; }
  .frame-thick { stroke-width: 6; }
  .frame-thin { stroke-width: 3; }
  .panel-dark { fill: var(--charcoal); }
  .panel-teal { fill: var(--teal); }
  .leaf-pattern { fill: var(--leaf-tone); opacity: .35; }
  .brand-name { font-family: "Lilita One", sans-serif; fill: var(--teal); font-size: 46px; }
  .brand-tagline { font-family: "Lilita One", sans-serif; fill: var(--teal); font-size: 9px; letter-spacing: .3px; }
  .tea-name { font-family: "Lilita One", sans-serif; fill: var(--teal); font-size: 35px; letter-spacing: .5px; }
  .tea-subname { font-family: "Lilita One", sans-serif; fill: var(--teal); font-size: 21px; }
  .tea-size { font-family: "Roboto", sans-serif; fill: var(--teal); font-size: 11.7px; }
  .section-title { font-family: "Lilita One", sans-serif; fill: var(--white); font-size: 15.5px; letter-spacing: .4px; }
  .info-text { font-family: "Lilita One", sans-serif; fill: var(--white); font-size: 9.5px; letter-spacing: .2px; }
  .icon-ring { fill: none; stroke: var(--white); stroke-width: 1.6; }
  .icon-glyph { fill: var(--white); stroke: none; }
  .icon-stroke { fill: none; stroke: var(--white); stroke-width: 1.4; stroke-linecap: round; }
  .teal-mark { fill: var(--teal); }
  .teal-stroke { fill: none; stroke: var(--teal); stroke-width: 2.5; }
</style>
</head>
<body>
<svg class="label-sheet" viewBox="0 0 1280 800" xmlns="http://www.w3.org/2000/svg">

  <!-- Front label -->
  <g class="front-label">
    <g class="front-frame">
      <line class="frame-line frame-thin" x1="244" y1="120" x2="244" y2="730"/>
      <line class="frame-line frame-thin" x1="556" y1="120" x2="556" y2="730"/>
      <line class="frame-line frame-thick" x1="257" y1="90" x2="257" y2="765"/>
      <line class="frame-line frame-thick" x1="544" y1="90" x2="544" y2="765"/>
      <line class="frame-line frame-thin" x1="257" y1="104" x2="544" y2="104"/>
      <line class="frame-line frame-thick" x1="232" y1="119" x2="568" y2="119"/>
      <line class="frame-line frame-thick" x1="232" y1="731" x2="568" y2="731"/>
      <line class="frame-line frame-thin" x1="257" y1="745" x2="544" y2="745"/>
    </g>

    <rect class="panel-dark" x="260" y="123" width="281" height="229"/>
    <rect class="panel-teal" x="255" y="352" width="291" height="375" role="img" aria-label="Fine dotted teal pattern"/>
    <rect class="panel-dark" x="276" y="405" width="250" height="322"/>
    <polygon class="teal-mark" points="303,405 313,405 308,411"/>

    <line class="header-rule teal-stroke" x1="260" y1="184" x2="541" y2="184"/>

    <g class="brand-block">
      <circle class="teal-mark" cx="311" cy="275" r="9"/>
      <text class="brand-name" x="410" y="286" text-anchor="middle">Brewlark</text>
      <text class="brand-tagline" x="408" y="303" text-anchor="middle">DISCOVER LOOSE LEAF TEA AT ITS BRIGHTEST</text>
    </g>

    <g class="detail-markers">
      <polygon class="teal-mark" points="303,445 313,445 308,452"/>
      <polygon class="teal-mark" points="303,485 313,485 308,492"/>
      <polygon class="teal-mark" points="303,525 313,525 308,532"/>
      <polygon class="teal-mark" points="303,565 313,565 308,572"/>
    </g>

    <text class="tea-name" x="297" y="629">BLUEBERRY</text>
    <text class="tea-subname" x="297" y="648">BURST</text>
    <text class="tea-size" x="297" y="675">(100G) 38-50 SERVINGS</text>
  </g>

  <!-- Back label -->
  <g class="back-label">
    <g class="back-frame">
      <rect class="frame-line frame-thick" x="605" y="86" width="337" height="676"/>
      <line class="frame-line frame-thin" x1="615" y1="114" x2="615" y2="731"/>
      <line class="frame-line frame-thin" x1="623" y1="114" x2="623" y2="731"/>
      <line class="frame-line frame-thin" x1="922" y1="114" x2="922" y2="731"/>
      <line class="frame-line frame-thin" x1="934" y1="114" x2="934" y2="731"/>
      <line class="frame-line frame-thick" x1="629" y1="86" x2="629" y2="762"/>
      <line class="frame-line frame-thick" x1="916" y1="86" x2="916" y2="762"/>
      <line class="frame-line frame-thin" x1="629" y1="101" x2="916" y2="101"/>
      <line class="frame-line frame-thick" x1="605" y1="116" x2="942" y2="116"/>
      <line class="frame-line frame-thick" x1="605" y1="730" x2="942" y2="730"/>
      <line class="frame-line frame-thin" x1="629" y1="745" x2="916" y2="745"/>
    </g>

    <rect class="panel-dark" x="632" y="119" width="281" height="608"/>
    <rect class="leaf-pattern" x="632" y="119" width="281" height="608" role="img" aria-label="Outlined tea leaf sprigs scattered across the panel"/>

    <text class="section-title" x="773" y="293" text-anchor="middle">STEEPING SUGGESTIONS</text>

    <g class="steep-icons">
      <circle class="icon-ring" cx="685" cy="326" r="10"/>
      <ellipse class="icon-glyph" cx="685" cy="322" rx="3" ry="4"/>
      <rect class="icon-glyph" x="684" y="325" width="2" height="8"/>

      <circle class="icon-ring" cx="777" cy="326" r="10"/>
      <rect class="icon-glyph" x="776" y="319" width="2" height="9"/>
      <circle class="icon-glyph" cx="777" cy="330" r="2.5"/>

      <circle class="icon-ring" cx="869" cy="326" r="10"/>
      <circle class="icon-stroke" cx="869" cy="326" r="5.5"/>
      <path class="icon-stroke" d="M869 323 v3 h3"/>
    </g>
    <text class="info-text" x="686" y="351" text-anchor="middle">1 1/2 TSP PER 8 OZ</text>
    <text class="info-text" x="779" y="351" text-anchor="middle">BOILING (212°)</text>
    <text class="info-text" x="869" y="351" text-anchor="middle">3 1/2-5 MINUTES</text>

    <text class="section-title" x="773" y="399" text-anchor="middle">TEA LATTE (1 SERVING)</text>

    <g class="latte-list">
      <circle class="icon-ring" cx="652" cy="426" r="10"/>
      <rect class="icon-glyph" x="649" y="421" width="6" height="10" rx="1.5"/>
      <rect class="icon-glyph" x="650.5" y="418" width="3" height="3"/>
      <text class="info-text" x="672" y="429">1/2 CUP STEAMED MILK</text>

      <circle class="icon-ring" cx="652" cy="461" r="10"/>
      <circle class="icon-glyph" cx="649" cy="458" r="1"/>
      <circle class="icon-glyph" cx="655" cy="459" r="1"/>
      <circle class="icon-glyph" cx="650" cy="464" r="1"/>
      <circle class="icon-glyph" cx="655" cy="464" r="1"/>
      <text class="info-text" x="672" y="458">1/2 TSP. SUGAR</text>
      <text class="info-text" x="672" y="470">OR CONDENSED MILK</text>

      <circle class="icon-ring" cx="652" cy="496" r="10"/>
      <path class="icon-glyph" d="M652 489 q5 7 3.5 9.5 a3.8 3.8 0 0 1 -7 0 q-1.5 -2.5 3.5 -9.5 z"/>
      <text class="info-text" x="668" y="501">1 CUP WATER</text>

      <circle class="icon-ring" cx="652" cy="531" r="10"/>
      <ellipse class="icon-glyph" cx="652" cy="527" rx="3" ry="4"/>
      <rect class="icon-glyph" x="651" y="530" width="2" height="8"/>
      <text class="info-text" x="668" y="534">3 TSP. TEA</text>
    </g>

    <text class="info-text" x="788" y="566" text-anchor="middle">STEEP IN WATER AND ADD TO STEAMED MILK.  ENJOY!</text>
  </g>
</svg>
</body>
</html>
```